Looking for a cool & simple business-card-design for digital agency

Hi!

We are a web agency that offers Reputation Management, Zorvik & Seo Services and software development. We like cool things, we like innovative styles.

We have uploaded our logo.

Project Deadline Extended Reason: Client does not want any designs with the colorful logo. Please send us submissions ONLY with the blac and white logo. What the client would like to see:1) Back of the card: is a silver logo on a black background2) front of the card with all the data, please use white background and black logo thank you Added Friday, May 8, 2015

Software

```html
<!DOCTYPE html>
<html lang="de">
<head>
<meta charset="utf-8">
<title>Nexaro AG – Visitenkarten</title>
<link rel="stylesheet" href="https://fonts.googleapis.com/css2?family=Orbitron:wght@400;900&family=Almendra&display=swap">
<style>
  :root {
    --page: #ffffff;
    --front-bg: #ffffff;
    --front-border: #d9d9d9;
    --front-texture-a: #ececec;
    --front-texture-b: #f6f6f6;
    --back-bg: #0b0b0b;
    --back-texture-a: #1c1c1e;
    --back-texture-b: #141414;
    --ink: #0a0a0a;
    --silver: #c4c4c8;
    --contact: #2b2b2b;
    --accent: #e3e020;
  }
  html, body {
    margin: 0;
    padding: 0;
    width: 1200px;
    height: 1000px;
    overflow: hidden;
    background: var(--page);
  }
  .canvas {
    position: relative;
    width: 1200px;
    height: 1000px;
  }
  .card {
    position: absolute;
    overflow: hidden;
    box-sizing: border-box;
  }
  .card--front {
    left: 106px; top: 100px; width: 750px; height: 375px;
    background: var(--front-bg);
    border: 1px solid var(--front-border);
    color: var(--ink);
  }
  .card--back {
    left: 412px; top: 490px; width: 752px; height: 380px;
    background: var(--back-bg);
    color: var(--silver);
  }

  .texture {
    position: absolute;
    top: 0;
    left: 14px;
    width: 390px;
  }
  .card--front .texture { height: 375px; }
  .card--back .texture  { height: 380px; }

  .accent-line {
    position: absolute;
    left: 0;
    right: 0;
    height: 3px;
    background: var(--accent);
  }
  .card--front .accent-line { top: 333px; }
  .card--back .accent-line  { top: 339px; }

  .brand-mark {
    position: absolute;
    background: currentColor;
  }
  .brand-name,
  .brand-tagline {
    position: absolute;
    margin: 0;
    line-height: 1;
    font-family: "Orbitron", sans-serif;
    color: currentColor;
    white-space: nowrap;
  }
  .brand-name { font-weight: 900; }
  .brand-tagline { font-weight: 400; }

  .card--front .brand-mark    { left: 40px; top: 162px; width: 48px; height: 48px; }
  .card--front .brand-name    { left: 106px; top: 150px; font-size: 34px; letter-spacing: 2px; }
  .card--front .brand-tagline { left: 106px; top: 188px; font-size: 14px; letter-spacing: 4.5px; }

  .card--back .brand-mark    { left: 48px; top: 138px; width: 78px; height: 78px; }
  .card--back .brand-name    { left: 173px; top: 134px; font-size: 58px; letter-spacing: 8px; }
  .card--back .brand-tagline { left: 173px; top: 198px; font-size: 23px; letter-spacing: 9px; }

  .contact {
    position: absolute;
    left: 400px;
    top: 124px;
    margin: 0;
    padding: 0;
    list-style: none;
    font-family: "Almendra", serif;
    color: var(--contact);
  }
  .contact li { line-height: 34px; font-size: 26px; }
  .contact .contact-web { font-size: 23px; line-height: 28px; margin-top: 10px; }
</style>
</head>
<body>
<main class="canvas">

  <section class="card card--front" aria-label="Vorderseite">
    <svg class="texture" viewBox="0 0 390 375" preserveAspectRatio="none" role="img" aria-label="Grunge-Silhouette als dezente Hintergrundtextur">
      <defs>
        <linearGradient id="texture-front" x1="0" y1="0" x2="1" y2="1">
          <stop offset="0" stop-color="var(--front-texture-a)"/>
          <stop offset="1" stop-color="var(--front-texture-b)"/>
        </linearGradient>
      </defs>
      <rect width="390" height="375" fill="url(#texture-front)"/>
    </svg>
    <div class="brand-mark"></div>
    <h1 class="brand-name">Nexaro AG</h1>
    <p class="brand-tagline">DIGITALE STRATEGIEN</p>
    <ul class="contact">
      <li>Email:</li>
      <li>Tel :</li>
      <li class="contact-web">www.nexaroag.com</li>
    </ul>
    <div class="accent-line"></div>
  </section>

  <section class="card card--back" aria-label="Rückseite">
    <svg class="texture" viewBox="0 0 390 380" preserveAspectRatio="none" role="img" aria-label="Grunge-Silhouette als dezente Hintergrundtextur">
      <defs>
        <linearGradient id="texture-back" x1="0" y1="0" x2="1" y2="1">
          <stop offset="0" stop-color="var(--back-texture-a)"/>
          <stop offset="1" stop-color="var(--back-texture-b)"/>
        </linearGradient>
      </defs>
      <rect width="390" height="380" fill="url(#texture-back)"/>
    </svg>
    <div class="brand-mark"></div>
    <h2 class="brand-name">Nexaro AG</h2>
    <p class="brand-tagline">DIGITALE STRATEGIEN</p>
    <div class="accent-line"></div>
  </section>

</main>
</body>
</html>
```